Electrical & Communications Company Wordpress Themed Website Design

Hi everyone,

I need a wordpress themed website designed for a new company based in Sydney Australia called "VELTRIX". It delivers electrical and communication services to the domestic and commercial sectors.

It needs to be the FULL/COMPLETE wordpress theme! A clean and easy to use site.

Please guys take the time to look at these competitors sites:

www.tapnovo.com.au
www.harbelwiring.com.au
www.qul.com.au
www.lumavoltics.com.au
www.corbinwiring.com.au
www.fendrasparkies.com.au

Please use these site for ideas only!!! we want to be original.

(If you would like to add electrical and communications to the logo that is O.K.)

Note: These logo's are registered trademarks of veltrix pty ltd.

Accreditation:

Ubta member (Federated wiring and signalling guild)

PLEASE CHECK THE WEB PLANNING LAYOUT BELOW FOR ROUGH IDEA
Updates

Have requested to increase payment to $400 and now guarantee payment!

Hi guys, forgot to mention i would like to see the business phone number prominently some where with a call to action.As we are a service business and need people to easly be able to see our contact number. Maybe top right courner but open to ideas. 

 Guys/Girls this is for a complete working word press theme that i can load up on the sever and access thru wordpress admin. Code etc

Industry/Entity Type

Communications

Requirements
Must have
• - Logo Provided must be used
• - Themes and colours to be consisted with with brand
• - Fully customizable
• - Have a social share button from shariq.com
• - Must be the full/complete theme for word press
Nice to have
• - pixtorvault
• - contactform
• - would like zenda orbit pay quidlo displayed
• - Guarantee logo or something
Should not have
• - Please don't waste your or our time submitting templates or copies of other sites original only!

```html
<!DOCTYPE html>
<html lang="en">
<head>
<meta charset="utf-8">
<title>VELTRIX – Electrical &amp; Communications</title>
<link href="https://fonts.googleapis.com/css2?family=PT+Sans:wght@400;700&family=Arimo:wght@400;700&display=swap" rel="stylesheet">
<style>
:root{
  --red:#e4101e;
  --red-dark:#a8060f;
  --ink:#333;
  --muted:#5a5a5a;
  --grey-text:#7a7a7a;
  --panel:#f0f0f0;
  --panel-edge:#dcdcdc;
  --page:#e9e9e9;
  --band:#5b5b5b;
  --white:#fff;
  --footer:#141414;
}
*{box-sizing:border-box;margin:0;padding:0}
html,body{width:1093px;height:1200px;overflow:hidden}
body{position:relative;background:linear-gradient(var(--band) 0,#707070 215px,var(--page) 216px);font-family:"Arimo",Arial,sans-serif;color:var(--ink)}
.abs{position:absolute}
.site{position:absolute;left:32px;top:21px;width:1027px;height:1179px;background:#f5f5f5}
.header{position:absolute;left:0;top:0;width:1027px;height:124px;background:var(--white)}
.brand{position:absolute;left:18px;top:26px;display:flex;align-items:center;gap:12px}
.brand-mark{width:58px;height:58px;border-radius:50%;background:var(--red)}
.brand-name{font-family:"PT Sans",sans-serif;font-weight:700;font-size:52px;color:var(--red);letter-spacing:1px}
.social{position:absolute;right:30px;top:12px;display:flex;gap:10px}
.social span{width:24px;height:24px;border-radius:4px;background:#8a8a8a}
.toplinks{position:absolute;right:34px;top:50px;font-family:"PT Sans",sans-serif;font-size:14px;color:var(--muted)}
.toplinks b{font-weight:400;margin:0 5px;color:#aaa}
.callus{position:absolute;right:30px;top:66px;font-family:"PT Sans",sans-serif;font-size:48px;color:#555}
.callus em{font-style:normal;color:var(--red)}
.nav{position:absolute;left:0;top:124px;width:1027px;height:35px;background:linear-gradient(#fafafa,#e2e2e2);border-top:1px solid #ddd;border-bottom:1px solid #ccc;display:flex;align-items:center;font-family:"PT Sans",sans-serif;font-size:19px;color:#666}
.nav a{color:inherit;text-decoration:none;padding:2px 6px;margin:0 7px}
.nav a.active{background:linear-gradient(#e4101e,#a8060f);color:var(--white);border:1px solid #fff}
.panel{position:absolute;background:linear-gradient(var(--panel),#e4e4e4);border:1px solid var(--panel-edge);overflow:hidden}
.hero-frame{left:6px;top:169px;width:730px;height:328px;background:var(--white);border-radius:14px;box-shadow:0 2px 6px rgba(0,0,0,.4)}
.hero{position:absolute;left:9px;top:9px;width:712px;height:310px;border-radius:12px;background:linear-gradient(110deg,#5a1a10,#c75a1a 35%,#3c3c3c 60%,#222)}
.hero-cap{position:absolute;padding:4px 18px;text-align:center;background:rgba(255,255,255,.55);font-family:"PT Sans",sans-serif;font-size:22px;line-height:31px;color:#111}
.side h3{font-family:"PT Sans",sans-serif;font-weight:400;font-size:17px;line-height:22px;color:var(--red);white-space:nowrap}
.side p{font-size:14px;line-height:22px;color:#444}
.agent{position:absolute;left:10px;top:8px;width:94px;height:82px;background:linear-gradient(#e8d4c6,#b7765a)}
.field{display:block;width:208px;height:26px;border:1px solid #ccc;background:#fff;font-size:13px;color:#555;padding:4px 10px;margin-bottom:12px}
.btn{display:inline-block;background:linear-gradient(#f0141f,#b00610);color:#fff;font-family:"PT Sans",sans-serif;font-size:21px;text-align:center;border:1px solid #900}
.welcome h1{font-family:"PT Sans",sans-serif;font-weight:400;font-size:26px;line-height:44px;color:#111}
.welcome h1 span{font-size:40px;font-style:italic;font-weight:700;color:var(--red)}
.welcome p{font-size:14px;line-height:24.5px;letter-spacing:1.6px;color:var(--grey-text);margin-top:5px}
.box-title{font-family:"PT Sans",sans-serif;font-size:20px;line-height:26px;color:var(--red);display:flex;align-items:center;gap:10px}
.box-title::before{content:"";border-left:7px solid var(--red);border-top:5px solid transparent;border-bottom:5px solid transparent}
.quote{font-size:14px;line-height:28px;color:#333}
.badge{position:absolute;top:68px;width:99px;height:69px;background:#fff;border:1px solid #ddd}
.badge i{position:absolute;left:24px;top:11px;width:50px;height:46px;border-radius:50%;background:#d5d5d5}
.post{margin-top:8px}
.post h4{font-family:"PT Sans",sans-serif;font-weight:400;font-size:18px;line-height:24px;color:#222;display:flex;align-items:center;gap:12px}
.post h4::before{content:"";border-left:7px solid var(--red);border-top:5px solid transparent;border-bottom:5px solid transparent}
.post p{font-size:14px;line-height:21px;color:#444;padding-left:26px}
.footer{position:absolute;left:0;top:1072px;width:1027px;height:107px;background:linear-gradient(#2b2b2b,var(--footer));color:#fff}
.footer .cta{position:absolute;left:16px;top:8px;font-family:"PT Sans",sans-serif;font-size:20px}
.footer .copy{position:absolute;left:16px;top:47px;font-size:14px}
.footer .links{position:absolute;left:16px;top:77px;font-size:14px}
.cards{position:absolute;right:34px;top:28px;display:flex;gap:10px}
.cards span{width:62px;height:44px;background:#eee;border-radius:4px;color:#333;font-size:12px;font-weight:700;display:flex;align-items:center;justify-content:center}
</style>
</head>
<body>
<div class="site">
  <header class="header">
    <div class="brand"><span class="brand-mark"></span><span class="brand-name">VELTRIX</span></div>
    <div class="social" aria-label="Social share buttons"><span></span><span></span><span></span><span></span><span></span><span></span></div>
    <div class="toplinks">Home<b>|</b>Contact us<b>|</b>Careers</div>
    <div class="callus"><em>Call us:</em> 000-000-0000</div>
  </header>
  <nav class="nav">
    <a>Who we are</a><a>Our Services</a><a>Domestic</a><a class="active">Commercial sectors</a><a>Our Experience</a><a>Our Guarantee</a><a>Client Satisfaction</a>
  </nav>

  <div class="abs hero-frame">
    <div class="hero" role="img" aria-label="Close-up photo of an electrical switchboard with red indicator lights"></div>
    <div class="hero-cap" style="right:19px;bottom:22px">Don't worry your safety is our motto<br>we are always with you</div>
  </div>

  <aside class="side">
    <div class="panel" style="left:748px;top:175px;width:272px;height:101px">
      <div class="agent" role="img" aria-label="Photo of a support agent with a headset"></div>
      <h3 class="abs" style="left:116px;top:14px;font-size:16px">You Need Our Help?</h3>
      <p class="abs" style="left:116px;top:42px">We are available 24<br>Hours 7 Days a Week</p>
    </div>
    <div class="panel" style="left:748px;top:289px;width:272px;height:101px;padding:7px 10px">
      <h3 style="font-size:16px">No callout Fees No fix, pay policy.</h3>
      <p style="font-size:13px;line-height:21px;margin-top:2px">We have the ultimate array of services to provide you a fast and low cost home or offices.</p>
    </div>
    <div class="panel" style="left:748px;top:400px;width:272px;height:97px;padding:8px 10px">
      <h3 style="font-size:19px;line-height:24px">Fixed Pricing</h3>
      <p style="margin-top:4px;line-height:26px;font-size:13.5px">We'll give you a guaranteed fixed price for any of your requirements</p>
    </div>
    <div class="panel" style="left:748px;top:512px;width:272px;height:150px;padding:10px 10px">
      <h3 style="margin-bottom:10px">Connect with us</h3>
      <span class="field">Enter Your Email</span>
      <span class="field">Enter Your Phone Number</span>
      <span class="btn" style="width:106px;height:30px;line-height:28px">SEND</span>
    </div>
    <div class="panel" style="left:748px;top:678px;width:272px;height:49px;padding:10px 10px;display:flex;gap:8px">
      <span class="field" style="width:174px;margin:0">Enter Search key words</span>
      <span class="btn" style="width:74px;height:26px;font-size:18px;line-height:24px">SEARCH</span>
    </div>
    <div class="panel" style="left:748px;top:741px;width:272px;height:304px;padding:8px 14px">
      <div class="box-title">Latest Blog Posts</div>
      <div class="post"><h4>Post sample Text here</h4><p>Sample text here Sample text here Sample text here Sample text here Sample text here Sample text here</p></div>
      <div class="post"><h4>Post sample Text here</h4><p>Sample text here Sample text here Sample text here Sample text here Sample text here Sample text here</p></div>
      <div class="post"><h4>Post sample Text here</h4><p>Sample text here Sample text here Sample text here Sample text here</p></div>
    </div>
  </aside>

  <section class="panel welcome" style="left:8px;top:512px;width:725px;height:327px;padding:10px 12px">
    <h1>WELCOME TO <span>VELTRIX</span></h1>
    <p>Our highly motivated team are rigorously trained and routinely tested for competency and compliance to ensure we meet stringent legislation requirements.Combine this with our company's comprehensive licensing and insurance, and you can be safe in the knowledge that Veltrix will deliver your electrical project to the highest possible standard that not only meets, but exceeds, today's stringent requirements.</p>
    <p>Our highly motivated team are rigorously trained and routinely tested for competency and compliance to ensure we meet stringent legislation requirements.Combine this with our company's comprehensive licensing and insurance, and you can be safe in the knowledge that Veltrix will deliver your electrical project to the highest possible standard that not only meets, but exceeds, today's stringent requirements.</p>
  </section>

  <section class="panel" style="left:8px;top:851px;width:272px;height:194px;padding:10px 10px">
    <div class="box-title">Testiamonial</div>
    <p class="quote" style="margin-top:4px">" VELTRIX have been contractors to Brindle Fabrication for several years. Their service and quality of work has been outstanding, from remedial works to large factory refits.Dane Carrow "</p>
  </section>

  <section class="panel" style="left:290px;top:851px;width:443px;height:194px;padding:10px 10px">
    <div class="box-title">Puch line to here</div>
    <div class="badge" style="left:6px" role="img" aria-label="Ubta member badge"><i></i></div>
    <div class="badge" style="left:108px" role="img" aria-label="Accreditation badge"><i></i></div>
    <div class="badge" style="left:222px" role="img" aria-label="Accreditation badge"><i></i></div>
    <div class="badge" style="left:333px" role="img" aria-label="Accreditation badge"><i style="border-radius:4px"></i></div>
  </section>

  <footer class="footer">
    <div class="cta">Call us today for a no obligation quote Links to contact form</div>
    <div class="copy">© copy right 2010 Veltrix All Rights Reserved.</div>
    <div class="links">Home | Who we are | Our Services | Contact Us</div>
    <div class="cards"><span>crestpay</span><span>zenda</span><span>orbit pay</span><span>paycheq</span></div>
  </footer>
</div>
</body>
</html>
```